Vora Leave In Conditioning Mist

The product is a 10oz light detangler in a continuous mister bottle. Trying to be an alternative to a competitor, "Brisk Lane Tidal Mist" https://brisklanehair.com/products/tidal-mist-leave-in-conditioner

The brand name is "Vora" or "VORA".
Product is a "10 in 1 Multi-Use Leave In Conditioner (lane mist)"
Featured ingredient is "Biotin" and "Keratin"

The art attached shows my attempt but it needs to be classier.

Label size is 6.75"W x 5.25"H (rounded edges).
Material is silver foil with matte finish overlay.

Thank you,
Theo

Vora

```html
<!DOCTYPE html>
<html lang="en">
<head>
<meta charset="utf-8">
<title>Vora Leave In Conditioning Mist – Label</title>
<link rel="stylesheet" href="https://fonts.googleapis.com/css2?family=Montserrat:wght@400;500;600&display=swap">
<style>
  :root {
    --backdrop: #d6d6d6;
    --biotin-blue: #1a9ed6;
    --biotin-blue-light: #3cc0ee;
    --biotin-blue-deep: #0f86bd;
    --keratin-red: #d0123f;
    --keratin-red-light: #ec3a63;
    --keratin-red-deep: #b00a33;
    --foil-light: #fbfbfb;
    --foil-mid: #d9dadc;
    --foil-dark: #a9abae;
    --ink-silver: #e9ecef;
    --brand-grey: #6a6c70;
    --pill-dark: #2b3a3f;
  }
  * { box-sizing: border-box; margin: 0; padding: 0; }
  html, body {
    width: 1200px;
    height: 848px;
    overflow: hidden;
  }
  body {
    background: radial-gradient(ellipse at center, #e6e6e6 0%, var(--backdrop) 60%, #c4c4c4 100%);
    font-family: "Montserrat", sans-serif;
    position: relative;
  }
  .label {
    position: absolute;
    top: 74px;
    width: 260px;
    height: 700px;
    border-radius: 18px;
    overflow: hidden;
    color: var(--ink-silver);
    text-align: center;
  }
  .label--biotin {
    left: 300px;
    background:
      repeating-linear-gradient(90deg, rgba(255,255,255,0) 0 14px, rgba(255,255,255,0.08) 14px 18px, rgba(0,0,0,0.04) 18px 30px),
      linear-gradient(90deg, var(--biotin-blue-deep) 0%, var(--biotin-blue-light) 30%, var(--biotin-blue) 55%, var(--biotin-blue-light) 78%, var(--biotin-blue-deep) 100%);
  }
  .label--keratin {
    left: 640px;
    background:
      repeating-linear-gradient(90deg, rgba(255,255,255,0) 0 14px, rgba(255,255,255,0.08) 14px 18px, rgba(0,0,0,0.04) 18px 30px),
      linear-gradient(90deg, var(--keratin-red-deep) 0%, var(--keratin-red-light) 30%, var(--keratin-red) 55%, var(--keratin-red-light) 78%, var(--keratin-red-deep) 100%);
  }
  .label > * { position: absolute; left: 0; right: 0; white-space: nowrap; }

  .brand-tab {
    left: 43px;
    right: 43px;
    top: 0;
    height: 124px;
    border-radius: 0 0 14px 14px;
    background: linear-gradient(90deg, var(--foil-dark) 0%, var(--foil-light) 22%, var(--foil-mid) 45%, var(--foil-light) 68%, var(--foil-dark) 100%);
    border: 3px solid rgba(255,255,255,0.7);
    border-top: none;
    display: flex;
    align-items: center;
    justify-content: center;
    padding-top: 22px;
  }
  .brand-name {
    font-weight: 400;
    font-size: 42px;
    letter-spacing: 2px;
    color: var(--brand-grey);
  }
  .count {
    top: 158px;
    font-weight: 600;
    font-size: 27px;
    letter-spacing: 9px;
    padding-left: 9px;
  }
  .product-name {
    top: 204px;
    font-weight: 500;
    font-size: 74px;
    line-height: 1;
    letter-spacing: -1px;
  }
  .product-type {
    top: 290px;
    font-weight: 600;
    font-size: 44px;
    letter-spacing: 8px;
    padding-left: 8px;
    line-height: 1;
  }
  .tagline {
    top: 346px;
    font-weight: 500;
    font-size: 13.5px;
    letter-spacing: 1px;
  }
  .formula-pill {
    left: 16px;
    right: 16px;
    top: 384px;
    height: 34px;
    border-radius: 17px;
    border: 2px solid rgba(255,255,255,0.75);
    background: linear-gradient(90deg, var(--pill-dark) 0%, #55676c 50%, var(--pill-dark) 100%);
    font-weight: 500;
    font-size: 12.5px;
    letter-spacing: 0.4px;
    line-height: 30px;
  }
  .label--keratin .formula-pill {
    background: linear-gradient(90deg, #3a2a2e 0%, #6b5a5e 50%, #3a2a2e 100%);
  }
  .benefits-line {
    top: 438px;
    font-weight: 500;
    font-size: 13px;
    letter-spacing: 1px;
  }
  .seals {
    top: 482px;
    display: flex;
    justify-content: center;
    gap: 16px;
  }
  .seal {
    width: 56px;
    height: 56px;
    border-radius: 50%;
    border: 2px solid var(--ink-silver);
    box-shadow: inset 0 0 0 6px rgba(255,255,255,0.12);
  }
  .claims {
    top: 552px;
    font-weight: 500;
    font-size: 13.5px;
    line-height: 20px;
  }
  .volume {
    top: 642px;
    font-weight: 400;
    font-size: 18px;
  }
</style>
</head>
<body>

  <section class="label label--biotin">
    <div class="brand-tab"><span class="brand-name">VORA</span></div>
    <p class="count">10-IN-1</p>
    <h1 class="product-name">LANE</h1>
    <p class="product-type">MIST</p>
    <p class="tagline">MULTI-USE LEAVE IN</p>
    <p class="formula-pill">BIOTIN INFUSED FORMULA</p>
    <p class="benefits-line">BRIGHTEN - REVIVE - EVERYDAY</p>
    <div class="seals">
      <span class="seal" role="img" aria-label="Salon formula seal"></span>
      <span class="seal" role="img" aria-label="Sulfate free seal"></span>
      <span class="seal" role="img" aria-label="Paraben free seal"></span>
    </div>
    <p class="claims">Moisturize / Detangle / Breakage<br>Shine / Hydrate / Split Ends<br>Frizz Control / Smooth Cuticle<br>Strengthen / UV Protection</p>
    <p class="volume">10oz / 295mL</p>
  </section>

  <section class="label label--keratin">
    <div class="brand-tab"><span class="brand-name">VORA</span></div>
    <p class="count">10-IN-1</p>
    <h1 class="product-name">LANE</h1>
    <p class="product-type">MIST</p>
    <p class="tagline">MULTI-USE LEAVE IN</p>
    <p class="formula-pill">KERATIN INFUSED FORMULA</p>
    <p class="benefits-line">BRIGHTEN - REVIVE - EVERYDAY</p>
    <div class="seals">
      <span class="seal" role="img" aria-label="Salon formula seal"></span>
      <span class="seal" role="img" aria-label="Sulfate free seal"></span>
      <span class="seal" role="img" aria-label="Paraben free seal"></span>
    </div>
    <p class="claims">Moisturize / Detangle / Breakage<br>Shine / Hydrate / Split Ends<br>Frizz Control / Smooth Cuticle<br>Strengthen / UV Protection</p>
    <p class="volume">10oz / 295mL</p>
  </section>

</body>
</html>
```